MArketing Flyers Design for Talvoro Engineering.

I would like to redesign our marketing and promotional flyers for Talvoro Engineering.
We have previous flyers which we would have a fresh vibrant look on .
This includes Flyers for the tests that we do. Company profile and company presentation.

```html
<!DOCTYPE html>
<html lang="en">
<head>
<meta charset="utf-8">
<title>Talvoro Engineering Flyers</title>
<link href="https://fonts.googleapis.com/css2?family=Poppins:wght@400;500;600;700;800&display=swap" rel="stylesheet">
<style>
:root{
  --navy:#25236b;
  --red:#9c1118;
  --red-dark:#7d0d12;
  --light:#ececf1;
  --white:#ffffff;
  --ink:#2a2a33;
  --stage:#3a3b3e;
}
*{margin:0;padding:0;box-sizing:border-box}
html,body{width:774px;height:1200px;overflow:hidden}
body{position:relative;background:var(--white);font-family:"Poppins",sans-serif;color:var(--ink)}
.stage{position:absolute;left:0;top:0;width:774px;height:632px;background:var(--stage)}
.flyer{position:absolute;width:347px;height:449px;background:var(--white);overflow:hidden;box-shadow:0 4px 14px rgba(0,0,0,.28)}
.flyer.small{transform:scale(.88);transform-origin:0 0}
.header-art{position:absolute;left:0;top:0;width:347px;height:175px}
.content-card{position:absolute;left:0;top:162px;width:347px;height:260px;background:var(--white);border-radius:18px 18px 0 0}
.photo{position:absolute;border-radius:50%}
.brand{position:absolute;display:flex;align-items:center;gap:5px}
.brand-dot{width:40px;height:40px;border-radius:50%;background:var(--navy);border:3px solid var(--white);box-shadow:0 0 0 1px #ccc}
.brand-name{font-weight:600;font-size:13px;line-height:1;color:var(--navy);width:82px}
.title{position:absolute;color:var(--white);font-weight:800;line-height:.95;text-transform:uppercase}
.title .big{font-size:23px;display:block;margin-bottom:2px}
.title .sub{font-size:13px;display:block}
.title.tank{font-size:16.5px;line-height:1}
.title.tank .case{text-transform:none}
.lead{position:absolute;left:26px;top:172px;width:300px;font-size:7.4px;font-weight:700;line-height:1.25;color:var(--navy);text-transform:uppercase}
.lead em{font-style:normal;color:var(--red)}
.checks{position:absolute;left:26px;top:194px;width:300px;list-style:none}
.checks li{position:relative;padding-left:12px;font-size:4.9px;line-height:1.3;margin-bottom:9px;color:var(--ink)}
.checks li::before{content:"";position:absolute;left:0;top:1px;width:6px;height:6px;border-radius:50%;background:var(--red)}
.checks li::after{content:"";position:absolute;left:1.8px;top:2.4px;width:2px;height:1.2px;border-left:1px solid #fff;border-bottom:1px solid #fff;transform:rotate(-45deg)}
.gallery{position:absolute;left:26px;top:320px;display:flex;gap:5px}
.gallery div{width:95px;height:79px;border-radius:6px}
.footer{position:absolute;left:0;bottom:0;width:347px;height:38px}
.footer-navy{position:absolute;left:0;top:0;width:347px;height:38px;background:var(--navy)}
.footer-red{position:absolute;left:165px;top:8px;width:182px;height:30px;background:var(--red);border-top-left-radius:12px}
.talk{position:absolute;left:28px;top:4px;color:var(--white)}
.talk small{display:block;font-size:7px;font-weight:500;letter-spacing:.2px}
.talk strong{display:flex;align-items:center;gap:3px;font-size:12px;font-weight:700;line-height:1.1}
.web{position:absolute;left:178px;top:17px;font-size:8.5px;color:var(--white);display:flex;align-items:center;gap:3px}
.corner-dot{position:absolute;right:-8px;bottom:-6px;width:44px;height:44px;border-radius:50%;background:var(--white)}
.about{position:absolute;left:28px;top:172px;width:192px;font-size:4.5px;line-height:1.28;text-align:justify;color:var(--ink)}
.about b{color:var(--navy)}
.media{position:absolute;border-radius:6px}
.adv-panel{position:absolute;left:34px;top:258px;width:286px;height:138px;background:var(--navy);border-radius:0 0 12px 0}
.adv-title{position:absolute;left:41px;top:264px;width:170px;font-size:7.4px;font-weight:700;line-height:1.25;color:var(--white);text-transform:uppercase}
.adv-list{position:absolute;left:26px;top:291px;list-style:none}
.adv-list li{display:flex;align-items:center;gap:12px;font-size:4.9px;font-weight:600;color:var(--white);height:14.6px;width:120px;line-height:1.2}
.adv-list li i{flex:none;width:10px;height:10px;border-radius:50%;background:var(--white);border:1.5px solid var(--red);position:relative}
.adv-list li i::after{content:"";position:absolute;left:2px;top:2px;width:3px;height:3px;border-radius:50%;background:var(--navy)}
</style>
</head>
<body>

<div class="stage"></div>

<!-- Piping inspection flyer template used at two sizes -->
<div class="flyer small" style="left:76px;top:104px">
  <svg class="header-art" viewBox="0 0 347 175" aria-hidden="true">
    <rect width="347" height="175" fill="var(--light)"/>
    <path d="M250,0 H347 V175 H250Z" fill="var(--navy)"/>
    <path d="M0,100 L14,84 L26,96 L44,70 L60,92 L80,80 L96,96 L118,62 L140,86 L160,74 L182,92 L205,68 L250,55 L250,175 L0,175Z" fill="var(--white)"/>
    <path d="M0,106 L14,90 L26,102 L44,76 L60,98 L80,86 L96,102 L118,68 L140,92 L160,80 L182,98 L205,74 L250,61 L250,175 L0,175Z" fill="var(--red)"/>
    <circle cx="255" cy="82" r="86" fill="var(--white)"/>
    <circle cx="255" cy="82" r="82" fill="var(--red)"/>
  </svg>
  <div class="photo" role="img" aria-label="Photo of steel process piping with valves and gauges" style="left:179px;top:6px;width:152px;height:152px;background:radial-gradient(circle at 45% 55%,#b8bcc2,#5d6570 55%,#2d333b)"></div>
  <div class="brand" style="left:26px;top:10px"><span class="brand-dot"></span><span class="brand-name">Talvoro Engineering</span></div>
  <div class="title" style="left:26px;top:96px"><span class="big">API 570</span><span class="sub">Piping Inspection<br>and Certification</span></div>
  <div class="content-card"></div>
  <p class="lead">This code covers inspection, repair, alteration, <em>and rerating procedures for in-service metallic piping systems.</em></p>
  <ul class="checks">
    <li>It establishes requirements and guidelines that allow owner/users of piping systems to maintain the safety and mechanical integrity of systems after they have been placed into service.</li>
    <li>This may be used, where practical, for any piping system.</li>
    <li>Piping inspectors are certified to API 570 as a well known inspection company with a high value on professional skills, Talvoro Inspection Services Co.,Ltd, provide API 570 Pipeline Inspection and Certification services within Kenya and around the world.</li>
    <li>Accuracy is ensured by the use of high technology data acquisition equipment giving certainty of data integrity.</li>
    <li>In addition all data will be collected in the database and handed to clients for further monitoring by themselves to aid with future planning by giving an inspection timeline.</li>
  </ul>
  <div class="gallery">
    <div role="img" aria-label="Inspector beside insulated pipework" style="background:linear-gradient(135deg,#c9a24a,#8d9097 60%,#4b5563)"></div>
    <div role="img" aria-label="Technician inspecting machinery" style="background:linear-gradient(135deg,#b5654a,#3f5f8a 60%,#5b3a2c)"></div>
    <div role="img" aria-label="White process pipes with gauges" style="background:linear-gradient(135deg,#e8ebee,#aab2bb 60%,#59636e)"></div>
  </div>
  <div class="footer">
    <div class="footer-navy"></div>
    <div class="footer-red"></div>
    <div class="talk"><small>TALK TO US:</small><strong><svg width="9" height="9" viewBox="0 0 24 24"><path fill="#fff" d="M6.6 10.8a15 15 0 0 0 6.6 6.6l2.2-2.2c.3-.3.7-.4 1-.2 1.1.4 2.3.6 3.6.6.6 0 1 .4 1 1V20c0 .6-.4 1-1 1A17 17 0 0 1 3 4c0-.6.4-1 1-1h3.5c.6 0 1 .4 1 1 0 1.3.2 2.5.6 3.6.1.3 0 .7-.2 1z"/></svg>+ 254 20 417 3920</strong></div>
    <div class="web"><svg width="7" height="7" viewBox="0 0 24 24"><circle cx="12" cy="12" r="10" fill="none" stroke="#fff" stroke-width="2"/><path d="M2 12h20M12 2c3 3 3 17 0 20M12 2c-3 3-3 17 0 20" fill="none" stroke="#fff" stroke-width="1.5"/></svg>www.talvoro-eng.com</div>
    <span class="corner-dot"></span>
  </div>
</div>

<!-- Tank calibration flyer -->
<div class="flyer small" style="left:413px;top:106px">
  <svg class="header-art" viewBox="0 0 347 175" aria-hidden="true">
    <rect width="347" height="175" fill="var(--light)"/>
    <path d="M0,0 H120 V175 H0Z" fill="var(--navy)"/>
    <path d="M120,85 L150,78 L170,96 L192,70 L210,88 L232,76 L250,92 L270,60 L290,80 L310,70 L330,50 L347,40 L347,175 L120,175Z" fill="var(--white)"/>
    <path d="M120,91 L150,84 L170,102 L192,76 L210,94 L232,82 L250,98 L270,66 L290,86 L310,76 L330,56 L347,46 L347,175 L120,175Z" fill="var(--red)"/>
    <circle cx="87" cy="87" r="92" fill="var(--white)"/>
    <circle cx="87" cy="87" r="88" fill="var(--red)"/>
  </svg>
  <div class="photo" role="img" aria-label="Photo of a refinery with storage tanks at dusk" style="left:5px;top:5px;width:164px;height:164px;background:linear-gradient(180deg,#4a4f86,#b07aa6 55%,#e6a36a 75%,#6a5a78)"></div>
  <div class="brand" style="left:200px;top:10px"><span class="brand-dot"></span><span class="brand-name">Talvoro Engineering</span></div>
  <div class="title tank" style="left:187px;top:93px">Horizontal<br>and Vertical<br>Storage Tank<br><span class="case">Calibration</span></div>
  <div class="content-card"></div>
  <p class="about"><b>Talvoro Engineering</b> Provides Tank calibration services using 3D laser scanner technology and geometrical and structural analysis aimed to verify the compliance with the relevant standards. The Tank calibrations conform to current measurement and calibration standards. Considering the dimensions, it is not correct to make a healthy tank measurement with classical measuring methods. We perform deformations mon the tank surfaces and measure the tank calibration by our high precision electro-optical measuring systems and 3D laser scanner devices. Our main services include anomalies in tank walls, solid tank model, tank volume, tank calibration measurement and linearity analysis. At the same time, these measurements can be combined with different NDT tests to create comprehensive observation reports.</p>
  <div class="media" role="img" aria-label="3D laser scanner inside a tank" style="left:228px;top:175px;width:92px;height:68px;background:radial-gradient(circle at 50% 60%,#4fa3c4,#1d2a44 60%,#0e1424)"></div>
  <div class="adv-panel"></div>
  <p class="adv-title">3D Laser Scanning Advantages on Tank Calibration Measurements.</p>
  <div class="media" role="img" aria-label="Colour point-cloud scan of a horizontal tank" style="left:229px;top:249px;width:91px;height:64px;background:radial-gradient(ellipse at 50% 45%,#f7c23a,#e0561d 45%,#111 75%);border:1.5px solid var(--white)"></div>
  <div class="media" role="img" aria-label="Laser scanner with tablet showing tank scan" style="left:162px;top:300px;width:138px;height:100px;background:linear-gradient(90deg,transparent,#9aa0a8 25%,#e6b325 50%,#2f3340 75%,transparent)"></div>
  <ul class="adv-list">
    <li><i></i>Minimizes Safety Risks</li>
    <li><i></i>Data Transferable to Modelling tools</li>
    <li><i></i>Avoids Manual Measurement errors.</li>
    <li><i></i>Accurate sump and bottom volume determination.</li>
    <li><i></i>Accracy increased as internal geometries are netted off.</li>
    <li><i></i>100% faster than usual methods</li>
    <li><i></i>NDT reporting.</li>
  </ul>
  <div class="footer">
    <div class="footer-navy"></div>
    <div class="footer-red"></div>
    <div class="talk"><small>TALK TO US:</small><strong><svg width="9" height="9" viewBox="0 0 24 24"><path fill="#fff" d="M6.6 10.8a15 15 0 0 0 6.6 6.6l2.2-2.2c.3-.3.7-.4 1-.2 1.1.4 2.3.6 3.6.6.6 0 1 .4 1 1V20c0 .6-.4 1-1 1A17 17 0 0 1 3 4c0-.6.4-1 1-1h3.5c.6 0 1 .4 1 1 0 1.3.2 2.5.6 3.6.1.3 0 .7-.2 1z"/></svg>+ 254 20 417 3920</strong></div>
    <div class="web"><svg width="7" height="7" viewBox="0 0 24 24"><circle cx="12" cy="12" r="10" fill="none" stroke="#fff" stroke-width="2"/><path d="M2 12h20M12 2c3 3 3 17 0 20M12 2c-3 3-3 17 0 20" fill="none" stroke="#fff" stroke-width="1.5"/></svg>www.talvoro-eng.com</div>
    <span class="corner-dot"></span>
  </div>
</div>

<!-- Full-size flat presentation -->
<div class="flyer" style="left:34px;top:677px">
  <svg class="header-art" viewBox="0 0 347 175" aria-hidden="true">
    <rect width="347" height="175" fill="var(--light)"/>
    <path d="M250,0 H347 V175 H250Z" fill="var(--navy)"/>
    <path d="M0,100 L14,84 L26,96 L44,70 L60,92 L80,80 L96,96 L118,62 L140,86 L160,74 L182,92 L205,68 L250,55 L250,175 L0,175Z" fill="var(--white)"/>
    <path d="M0,106 L14,90 L26,102 L44,76 L60,98 L80,86 L96,102 L118,68 L140,92 L160,80 L182,98 L205,74 L250,61 L250,175 L0,175Z" fill="var(--red)"/>
    <circle cx="255" cy="82" r="86" fill="var(--white)"/>
    <circle cx="255" cy="82" r="82" fill="var(--red)"/>
  </svg>
  <div class="photo" role="img" aria-label="Photo of steel process piping with valves and gauges" style="left:179px;top:6px;width:152px;height:152px;background:radial-gradient(circle at 45% 55%,#b8bcc2,#5d6570 55%,#2d333b)"></div>
  <div class="brand" style="left:26px;top:10px"><span class="brand-dot"></span><span class="brand-name">Talvoro Engineering</span></div>
  <div class="title" style="left:26px;top:96px"><span class="big">API 570</span><span class="sub">Piping Inspection<br>and Certification</span></div>
  <div class="content-card"></div>
  <p class="lead">This code covers inspection, repair, alteration, <em>and rerating procedures for in-service metallic piping systems.</em></p>
  <ul class="checks">
    <li>It establishes requirements and guidelines that allow owner/users of piping systems to maintain the safety and mechanical integrity of systems after they have been placed into service.</li>
    <li>This may be used, where practical, for any piping system.</li>
    <li>Piping inspectors are certified to API 570 as a well known inspection company with a high value on professional skills, Talvoro Inspection Services Co.,Ltd, provide API 570 Pipeline Inspection and Certification services within Kenya and around the world.</li>
    <li>Accuracy is ensured by the use of high technology data acquisition equipment giving certainty of data integrity.</li>
    <li>In addition all data will be collected in the database and handed to clients for further monitoring by themselves to aid with future planning by giving an inspection timeline.</li>
  </ul>
  <div class="gallery">
    <div role="img" aria-label="Inspector beside insulated pipework" style="background:linear-gradient(135deg,#c9a24a,#8d9097 60%,#4b5563)"></div>
    <div role="img" aria-label="Technician inspecting machinery" style="background:linear-gradient(135deg,#b5654a,#3f5f8a 60%,#5b3a2c)"></div>
    <div role="img" aria-label="White process pipes with gauges" style="background:linear-gradient(135deg,#e8ebee,#aab2bb 60%,#59636e)"></div>
  </div>
  <div class="footer">
    <div class="footer-navy"></div>
    <div class="footer-red"></div>
    <div class="talk"><small>TALK TO US:</small><strong><svg width="9" height="9" viewBox="0 0 24 24"><path fill="#fff" d="M6.6 10.8a15 15 0 0 0 6.6 6.6l2.2-2.2c.3-.3.7-.4 1-.2 1.1.4 2.3.6 3.6.6.6 0 1 .4 1 1V20c0 .6-.4 1-1 1A17 17 0 0 1 3 4c0-.6.4-1 1-1h3.5c.6 0 1 .4 1 1 0 1.3.2 2.5.6 3.6.1.3 0 .7-.2 1z"/></svg>+ 254 20 417 3920</strong></div>
    <div class="web"><svg width="7" height="7" viewBox="0 0 24 24"><circle cx="12" cy="12" r="10" fill="none" stroke="#fff" stroke-width="2"/><path d="M2 12h20M12 2c3 3 3 17 0 20M12 2c-3 3-3 17 0 20" fill="none" stroke="#fff" stroke-width="1.5"/></svg>www.talvoro-eng.com</div>
    <span class="corner-dot"></span>
  </div>
</div>

<div class="flyer" style="left:398px;top:677px">
  <svg class="header-art" viewBox="0 0 347 175" aria-hidden="true">
    <rect width="347" height="175" fill="var(--light)"/>
    <path d="M0,0 H120 V175 H0Z" fill="var(--navy)"/>
    <path d="M120,85 L150,78 L170,96 L192,70 L210,88 L232,76 L250,92 L270,60 L290,80 L310,70 L330,50 L347,40 L347,175 L120,175Z" fill="var(--white)"/>
    <path d="M120,91 L150,84 L170,102 L192,76 L210,94 L232,82 L250,98 L270,66 L290,86 L310,76 L330,56 L347,46 L347,175 L120,175Z" fill="var(--red)"/>
    <circle cx="87" cy="87" r="92" fill="var(--white)"/>
    <circle cx="87" cy="87" r="88" fill="var(--red)"/>
  </svg>
  <div class="photo" role="img" aria-label="Photo of a refinery with storage tanks at dusk" style="left:5px;top:5px;width:164px;height:164px;background:linear-gradient(180deg,#4a4f86,#b07aa6 55%,#e6a36a 75%,#6a5a78)"></div>
  <div class="brand" style="left:200px;top:10px"><span class="brand-dot"></span><span class="brand-name">Talvoro Engineering</span></div>
  <div class="title tank" style="left:187px;top:93px">Horizontal<br>and Vertical<br>Storage Tank<br><span class="case">Calibration</span></div>
  <div class="content-card"></div>
  <p class="about"><b>Talvoro Engineering</b> Provides Tank calibration services using 3D laser scanner technology and geometrical and structural analysis aimed to verify the compliance with the relevant standards. The Tank calibrations conform to current measurement and calibration standards. Considering the dimensions, it is not correct to make a healthy tank measurement with classical measuring methods. We perform deformations mon the tank surfaces and measure the tank calibration by our high precision electro-optical measuring systems and 3D laser scanner devices. Our main services include anomalies in tank walls, solid tank model, tank volume, tank calibration measurement and linearity analysis. At the same time, these measurements can be combined with different NDT tests to create comprehensive observation reports.</p>
  <div class="media" role="img" aria-label="3D laser scanner inside a tank" style="left:228px;top:175px;width:92px;height:68px;background:radial-gradient(circle at 50% 60%,#4fa3c4,#1d2a44 60%,#0e1424)"></div>
  <div class="adv-panel"></div>
  <p class="adv-title">3D Laser Scanning Advantages on Tank Calibration Measurements.</p>
  <div class="media" role="img" aria-label="Colour point-cloud scan of a horizontal tank" style="left:229px;top:249px;width:91px;height:64px;background:radial-gradient(ellipse at 50% 45%,#f7c23a,#e0561d 45%,#111 75%);border:1.5px solid var(--white)"></div>
  <div class="media" role="img" aria-label="Laser scanner with tablet showing tank scan" style="left:162px;top:300px;width:138px;height:100px;background:linear-gradient(90deg,transparent,#9aa0a8 25%,#e6b325 50%,#2f3340 75%,transparent)"></div>
  <ul class="adv-list">
    <li><i></i>Minimizes Safety Risks</li>
    <li><i></i>Data Transferable to Modelling tools</li>
    <li><i></i>Avoids Manual Measurement errors.</li>
    <li><i></i>Accurate sump and bottom volume determination.</li>
    <li><i></i>Accracy increased as internal geometries are netted off.</li>
    <li><i></i>100% faster than usual methods</li>
    <li><i></i>NDT reporting.</li>
  </ul>
  <div class="footer">
    <div class="footer-navy"></div>
    <div class="footer-red"></div>
    <div class="talk"><small>TALK TO US:</small><strong><svg width="9" height="9" viewBox="0 0 24 24"><path fill="#fff" d="M6.6 10.8a15 15 0 0 0 6.6 6.6l2.2-2.2c.3-.3.7-.4 1-.2 1.1.4 2.3.6 3.6.6.6 0 1 .4 1 1V20c0 .6-.4 1-1 1A17 17 0 0 1 3 4c0-.6.4-1 1-1h3.5c.6 0 1 .4 1 1 0 1.3.2 2.5.6 3.6.1.3 0 .7-.2 1z"/></svg>+ 254 20 417 3920</strong></div>
    <div class="web"><svg width="7" height="7" viewBox="0 0 24 24"><circle cx="12" cy="12" r="10" fill="none" stroke="#fff" stroke-width="2"/><path d="M2 12h20M12 2c3 3 3 17 0 20M12 2c-3 3-3 17 0 20" fill="none" stroke="#fff" stroke-width="1.5"/></svg>www.talvoro-eng.com</div>
    <span class="corner-dot"></span>
  </div>
</div>

</body>
</html>
```